CareerHUB Background Image Needed

I need a CareerHUB background image for my personal CareerHUB profile page. The dimension is 1400 pixels wide X 350 pixels high.

I am a consultant for www.RedMapleRun.com. The logo files are located here:

https://www.filecrate.net/sh/q7m3vtx2lpe8nwc4rbyaz/k?key=gn5wd2pxkv9tjhm4caqe81lr3&v=0

A single message in the background is:

"Give your business a Red Maple Run with a proven path to optimized sales"

```html
<!DOCTYPE html>
<html lang="en">
<head>
<meta charset="utf-8">
<title>Red Maple Run – Profile Banner</title>
<link rel="stylesheet" href="https://fonts.googleapis.com/css2?family=Federo&display=swap">
<style>
  :root {
    --bg-teal: #0b3544;
    --text-white: #ffffff;
    --text-outline: #0a1e26;
    --accent-red: #d2254b;
    --accent-red-dark: #8f1832;
  }
  html, body {
    margin: 0;
    padding: 0;
    overflow: hidden;
    background: var(--bg-teal);
  }
  .banner {
    position: relative;
    width: 1200px;
    height: 300px;
    background: var(--bg-teal);
    overflow: hidden;
  }
  .headline {
    position: absolute;
    left: 0;
    top: 0;
    width: 1200px;
    height: 300px;
  }
  .headline text {
    font-family: "Federo", sans-serif;
    fill: var(--text-white);
    stroke: var(--text-outline);
    stroke-width: 3px;
    paint-order: stroke fill;
    stroke-linejoin: round;
  }
  .exclamation-art {
    position: absolute;
    left: 806px;
    top: 88px;
    width: 58px;
    height: 122px;
    border-radius: 10px;
    background: linear-gradient(160deg, var(--accent-red) 0%, var(--accent-red) 60%, var(--accent-red-dark) 100%);
    transform: rotate(6deg);
  }
</style>
</head>
<body>
  <main class="banner">
    <svg class="headline" viewBox="0 0 1200 300" aria-label="Give your business a Red Maple Run with a proven path to optimized sales">
      <text class="headline__lead" x="415" y="105" font-size="30" textLength="372" lengthAdjust="spacingAndGlyphs">GIVE YOUR BUSINESS A RED</text>
      <text class="headline__brand" x="415" y="154" font-size="64" textLength="372" lengthAdjust="spacingAndGlyphs">MAPLE RUN</text>
      <text class="headline__bridge" x="415" y="180" font-size="30" textLength="372" lengthAdjust="spacingAndGlyphs">WITH A PROVEN PATH TO</text>
      <text class="headline__close" x="415" y="214" font-size="40" textLength="372" lengthAdjust="spacingAndGlyphs">OPTIMIZED SALES</text>
    </svg>
    <div class="exclamation-art" role="img" aria-label="Large red three-dimensional exclamation mark illustration"></div>
  </main>
</body>
</html>
```